依頼詳細
依頼したいものは、個包装のデザインと箱のデザインを依頼します。
ブランドのキーワードは、「貰って嬉しい手土産、自分へのご褒美、オーガニック、エレガント、特別、こだわり、幸福」です。
玉手箱、宝石のようなデザインが良いと思っています。
記載項目
①個包装サイズ:縦60mm 横90mm程度
下部はマチがあり立てられる仕様(イメージは添付をご確認ください。)

②箱サイズ:幅200mm 奥行110mm 高さ800mm
玉手箱のような箱
希望イメージ
シンプル 複雑
単色 カラフル
暗い 明るい
日常 高級
遊び心 厳粛
未来的 伝統的
女性的 男性的
希望する色
赤系
納品ファイル
• 高解像度JPG (.jpg)
• イラストレーター形式 (.ai)
• PNG形式 (.png)
補足説明
記載間違いによるサイズ修正です。

玉手箱のような箱

上記のサイズにて、高さは800mmではなく、80mmが正しい寸法です。
大変失礼いたしました。

気づいて下さりありがとうございます。
屋号のロゴデータになります。
テスト製作のものですが、商品のイメージが伝わればと思い、こちらも添付いたします。
締め切りの時間となりましたので、応募いただいたデザインより選定を進めさせていただきます。
たくさんの応募が集まり、非常に感謝しております。
吟味して選定したいと考えておりますので、今しばしお待ちいただければと思います。

ご応募いただきました皆様、本当にありがとうございます。
■ 選んだ理由

シンプルでありながら、見た瞬間に高級感を感じました。
このデザインをベースに紙質で高級感をさらに表現したいと思いました。
社内で最もファーストインプレッションがよかったデザインです。

■ 提案者全員のお礼・コメント

たくさんのご提案をいただき、誠にありがとうございました。
こちらでは想像できなかった斬新なデザインもあり、非常に参考になりました。
皆様のご提案を拝見したことで、我々もどんなデザインの箱がブランドイメージに最も合うのかも
わかりました。
改めて、たくさんのご提案をいただけたことに感謝を申し上げます。

```html
<!DOCTYPE html>
<html lang="ja">
<head>
<meta charset="utf-8">
<title>シュトーレン パッケージデザイン提案 C案</title>
<link rel="stylesheet" href="https://fonts.googleapis.com/css2?family=Noto+Sans+JP:wght@400;700&family=Noto+Serif+JP:wght@500&family=Playfair+Display:wght@700&display=swap">
<style>
  :root {
    --paper: #ffffff;
    --ink: #1c1c1c;
    --rule: #9a9a9a;
    --box-red: #5a1118;
    --box-red-deep: #440a10;
    --box-red-light: #6c1a21;
    --label: #fbf8f5;
    --label-line: #6a1a20;
    --chip-red: #7a1a22;
  }
  * { margin: 0; padding: 0; box-sizing: border-box; }
  html, body { width: 846px; height: 1200px; overflow: hidden; background: var(--paper); }
  .sheet { position: relative; width: 846px; height: 1200px; font-family: "Noto Sans JP", sans-serif; color: var(--ink); }

  .sheet-title { position: absolute; left: 78px; top: 76px; font-size: 21px; font-weight: 700; letter-spacing: 0.02em; }

  .colour-chip { position: absolute; left: 726px; top: 68px; width: 88px; text-align: center; }
  .colour-chip__swatch { height: 28px; background: var(--chip-red); color: #fff; font-size: 8px; line-height: 28px; }
  .colour-chip__code { margin-top: 5px; font-size: 8px; letter-spacing: 0.02em; }

  .variant-heading { position: absolute; left: 78px; top: 174px; font-size: 17px; font-weight: 700; }
  .heading-rule { position: absolute; left: 78px; right: 32px; top: 216px; height: 1px; background: var(--rule); }
  .finish-note { position: absolute; left: 78px; top: 234px; font-size: 11px; font-weight: 700; }

  .gift-box { position: absolute; left: 206px; top: 268px; width: 434px; height: 862px; overflow: hidden; }
  .gift-box__pattern { position: absolute; inset: 0;
    background: radial-gradient(ellipse at 50% 45%, var(--box-red-light) 0%, var(--box-red) 55%, var(--box-red-deep) 100%); }

  .name-label { position: absolute; left: 147px; top: 155px; width: 141px; height: 161px; background: var(--label); padding: 6px; }
  .name-label__frame { width: 100%; height: 100%; border: 2px solid var(--label-line); display: flex; flex-direction: column; align-items: center; color: var(--label-line); }
  .name-label__dot { width: 44px; height: 44px; margin-top: 14px; border-radius: 50%; border: 2px solid var(--label-line); }
  .name-label__name { margin-top: 12px; font-family: "Playfair Display", serif; font-weight: 700; font-size: 30px; line-height: 1; }
  .name-label__kana { margin-top: 8px; font-family: "Noto Serif JP", serif; font-size: 10px; letter-spacing: 0.1em; }

  .maker-tag { position: absolute; left: 189px; top: 621px; width: 56px; height: 42px; background: var(--label); display: flex; flex-direction: column; align-items: center; justify-content: center; gap: 4px; color: var(--label-line); }
  .maker-tag__dot { width: 10px; height: 10px; border-radius: 50%; background: var(--label-line); }
  .maker-tag__name { font-family: "Playfair Display", serif; font-weight: 700; font-size: 6px; letter-spacing: 0.08em; }
</style>
</head>
<body>
<main class="sheet">
  <h1 class="sheet-title">手土産商品「シュトーレン」様のパッケージデザイン提案</h1>

  <div class="colour-chip">
    <div class="colour-chip__swatch">レッドカラー</div>
    <div class="colour-chip__code">C0, M100, Y70, K50</div>
  </div>

  <h2 class="variant-heading">【C案】</h2>
  <div class="heading-rule"></div>
  <p class="finish-note">化粧箱(枠のグレーのラインは箔押しのシルバー or 色なしの箔押し、模様は色なしの箔押し or 印刷)</p>

  <section class="gift-box">
    <div class="gift-box__pattern" role="img" aria-label="深紅の地に色なし箔押しの菱形模様"></div>

    <div class="name-label">
      <div class="name-label__frame">
        <span class="name-label__dot"></span>
        <span class="name-label__name">Kleinod</span>
        <span class="name-label__kana">クライノート</span>
      </div>
    </div>

    <div class="maker-tag">
      <span class="maker-tag__dot"></span>
      <span class="maker-tag__name">ATELIER RIN</span>
    </div>
  </section>
</main>
</body>
</html>
```